Business card for denture clinic Gumlyssa

We need a new business card with our new logo. We are a denture clinic in New Zealand with our target market being 45+ years old. We would need a space on the back to write our patients next appointment on. We would space for only one appointment rather than a list. We will attach a photo showing an example of this. But of course, we would like to see your twist on this. We want it to be bold and easy to read and a good mixture of professional but modern. We have attached our logo to be used on the card.

Target Market(s)

People aged 45+ needing dentures

Industry/Entity Type

Dental

Contact Information for Business Card

We want our logo on the front and the space to write an appointment on the back. I've attached an example our our old business card showing this. We need to have the technicians details on the front.

Font styles to use
Sans Serif

Colors
0255a3
919191
fbfbfb

Requirements
Must have
• The following details:
• Ravi Pelling BDT, PGDipCDentTech Marlow
• Dental Prosthetist
• Phone numbers: 0800 47 2150
• 09 571 3294
• Email: ravi@gumlyssa.co.nz
• www.gumlyssa.co.nz
• Address: 418 Whiroa Road
• Kauriwhenua East
• Auckland 0610
Nice to have
• We would like our business cards to have more than just two colours as we want them to be more vibrant. We have uploaded an example of a business card we liked that showed this.

```html
<!DOCTYPE html>
<html lang="en">
<head>
<meta charset="utf-8">
<title>Gumlyssa – Business Card</title>
<link rel="stylesheet" href="https://fonts.googleapis.com/css2?family=Roboto:wght@300;400;500;700&display=swap">
<style>
  :root {
    --brand-blue: #0255a3;
    --band-blue: #1170bf;
    --grey: #919191;
    --ink: #2b2b2b;
    --paper: #fbfbfb;
    --stage: #e6e7e9;
  }
  * { box-sizing: border-box; margin: 0; padding: 0; }
  html, body {
    width: 1200px; height: 802px; overflow: hidden;
    background: var(--stage);
    font-family: "Roboto", Arial, sans-serif;
  }
  .sheet { position: relative; width: 1200px; height: 802px; }
  .card {
    position: absolute; top: 242px;
    width: 520px; height: 318px;
    background: var(--paper);
    box-shadow: 0 6px 18px rgba(0,0,0,.12);
    overflow: hidden;
  }
  .card--front { left: 50px; }
  .card--back { left: 630px; }

  /* Wordmark lockup */
  .brand { display: flex; align-items: center; gap: 10px; }
  .brand__square {
    width: 30px; height: 30px; background: var(--brand-blue); border-radius: 4px;
  }
  .brand__name {
    font-weight: 500; font-size: 30px; color: var(--brand-blue);
    letter-spacing: .5px;
  }

  /* Front */
  .card--front .brand { position: absolute; left: 32px; top: 140px; }
  .divider {
    position: absolute; left: 226px; top: 54px; width: 40px; height: 210px;
  }
  .details {
    position: absolute; left: 270px; top: 70px; right: 14px;
    color: var(--ink);
  }
  .details__name { font-size: 18px; font-weight: 400; white-space: nowrap; }
  .details__creds { font-size: 9.5px; color: #555; margin-left: 3px; }
  .details__role { font-size: 12.5px; color: var(--brand-blue); margin-top: 4px; }
  .details__address { font-size: 11.5px; line-height: 15px; margin-top: 5px; }
  .contact { list-style: none; margin-top: 5px; font-size: 11.5px; }
  .contact li { display: flex; align-items: center; gap: 6px; height: 16px; }
  .contact svg { width: 11px; height: 11px; flex: none; }

  /* Back */
  .card--back .brand {
    position: absolute; left: 0; right: 0; top: 62px;
    flex-direction: column; gap: 8px;
  }
  .card--back .brand__square { width: 44px; height: 44px; border-radius: 5px; }
  .card--back .brand__name { font-size: 34px; }
  .appointment {
    position: absolute; left: 0; right: 0; bottom: 0; height: 142px;
    background: var(--band-blue);
  }
  .appointment__title {
    text-align: center; color: #fff; font-size: 13px; font-weight: 400;
    letter-spacing: .6px; margin-top: 26px;
  }
  .appointment__fields {
    display: flex; justify-content: space-between;
    padding: 0 22px; margin-top: 20px;
  }
  .field {
    width: 220px; height: 42px; background: #fff; border-radius: 21px;
    display: flex; align-items: center; padding: 0 18px;
    color: #b5b5b5; font-size: 12px; font-weight: 300;
  }
  .field__slash { margin-left: 52px; }
</style>
</head>
<body>
<main class="sheet">

  <section class="card card--front" aria-label="Card front">
    <div class="brand">
      <span class="brand__square"></span>
      <span class="brand__name">Gumlyssa</span>
    </div>

    <svg class="divider" viewBox="0 0 40 210" aria-hidden="true">
      <defs>
        <linearGradient id="rule-fade" x1="0" y1="0" x2="0" y2="1">
          <stop offset="0" stop-color="#919191" stop-opacity="0"/>
          <stop offset=".5" stop-color="#919191" stop-opacity=".8"/>
          <stop offset="1" stop-color="#919191" stop-opacity="0"/>
        </linearGradient>
      </defs>
      <line x1="4" y1="0" x2="36" y2="210" stroke="url(#rule-fade)" stroke-width="1"/>
    </svg>

    <div class="details">
      <p class="details__name">Ravi Pelling<span class="details__creds">BDT, PGDipCDentTech Marlow</span></p>
      <p class="details__role">Dental Prosthetist</p>
      <p class="details__address">418 Whiroa Road<br>Kauriwhenua East, Auckland 0610</p>
      <ul class="contact">
        <li>
          <svg viewBox="0 0 12 12"><rect width="12" height="12" rx="2" fill="#0255a3"/><path d="M3.6 2.6l1.3 1.8-.8.9c.5 1 1.2 1.7 2.2 2.2l.9-.8 1.8 1.3-.6 1.2C6 9.1 2.9 6 2.4 3.2z" fill="#fff"/></svg>
          0800 47 2150
        </li>
        <li>
          <svg viewBox="0 0 12 12"><rect width="12" height="12" rx="2" fill="#0255a3"/><path d="M3.6 2.6l1.3 1.8-.8.9c.5 1 1.2 1.7 2.2 2.2l.9-.8 1.8 1.3-.6 1.2C6 9.1 2.9 6 2.4 3.2z" fill="#fff"/></svg>
          09 571 3294
        </li>
        <li>
          <svg viewBox="0 0 12 12"><rect x=".5" y=".5" width="11" height="11" rx="2" fill="none" stroke="#0255a3"/><rect x="3" y="4" width="6" height="4.4" fill="none" stroke="#0255a3" stroke-width=".9"/><path d="M3 4l3 2.3L9 4" fill="none" stroke="#0255a3" stroke-width=".9"/></svg>
          ravi@gumlyssa.co.nz
        </li>
        <li>
          <svg viewBox="0 0 12 12"><rect x=".5" y=".5" width="11" height="11" rx="2" fill="none" stroke="#0255a3"/><circle cx="6" cy="6" r="3.2" fill="none" stroke="#0255a3" stroke-width=".9"/><path d="M2.8 6h6.4M6 2.8c-1.6 1.8-1.6 4.6 0 6.4M6 2.8c1.6 1.8 1.6 4.6 0 6.4" fill="none" stroke="#0255a3" stroke-width=".7"/></svg>
          www.gumlyssa.co.nz
        </li>
      </ul>
    </div>
  </section>

  <section class="card card--back" aria-label="Card back">
    <div class="brand">
      <span class="brand__square"></span>
      <span class="brand__name">Gumlyssa</span>
    </div>

    <div class="appointment">
      <p class="appointment__title">YOUR NEXT APPOINTMENT</p>
      <div class="appointment__fields">
        <div class="field">Date<span class="field__slash">/</span><span class="field__slash">/</span></div>
        <div class="field">Time</div>
      </div>
    </div>
  </section>

</main>
</body>
</html>
```